Bright Path Academy - Personal Development business 2.0 needs a social post format design.

https://www.brightpathacademy-example.com

Our focus with Bright Path Academy is on developing people through knowledge and skills to improve their everyday lives.
We love simplicity, Quince design and less is more.

We are crazy about personal growth, science, design, the latest gadgets and people.

We need 4 formats for our social media posts.
1. Blogs -to pronounce a blog post
2. Workshop /training - to pronounce our workshops/trainings (both online and offline)
3. Podcast - called "Kijk eens verder". To pronounce a guest we've spoken. The host is called Berend.
4. Facts - to pronounce short facts about personal development. Invites people to read more.
The formats should include: high quality pictogram (better than the uploaded picto's), 1 of the 3 logo's in the design.
It's important that we can edit the design in Lumora Draw / Lumora Pixel to adjust the text in the format.

Attached you find four of our current designs, which are a poor example of how the designs should look like. These are just to show you how much lines of text (more or less) will be in the designs. So please do not make a design that looks like these ;) You have carte blanche.

Our customers are mostly women (80%). We focus on both business and casual customers.

Target Market(s)

80% woman, 20% men. We focus on both business and casual customers.

Requirements
Must have
• Less is more. Quince Design alike. Simplicity.
Aimed at the women target audience.
Designs must be edible for adjusting the text in the format.
Nice to have
• Unique concept.
The design should "breathe".
Each design can have a different color, so customers identify the specific post with specific information. For example, blog is red, workshop post black, etc.

```html
<!DOCTYPE html>
<html lang="nl">
<head>
<meta charset="utf-8">
<title>Bright Path Academy – social post formats</title>
<link rel="stylesheet" href="https://fonts.googleapis.com/css2?family=Signika:wght@300;400;700&display=swap">
<style>
  :root {
    --canvas: #ececec;
    --white: #ffffff;
    --podcast-deep: #0f2f55;
    --podcast-mid: #2a6aa6;
    --podcast-accent: #0a74c4;
    --training-deep: #0b0b0b;
    --training-mid: #5a5a5a;
    --training-accent: #1c1c1c;
    --blog-deep: #b97c10;
    --blog-mid: #f6b92e;
    --blog-accent: #ec8a26;
    --facts-deep: #0c3a1c;
    --facts-mid: #4a9566;
    --facts-accent: #137a43;
    --path-line: rgba(255,255,255,0.45);
  }
  * { box-sizing: border-box; margin: 0; padding: 0; }
  html, body { width: 1200px; height: 600px; overflow: hidden; background: var(--canvas); }
  body { font-family: "Signika", sans-serif; color: var(--white); position: relative; }

  .post { position: absolute; top: 165px; width: 271px; height: 271px; overflow: hidden; }
  .post--podcast  { left: 20px; }
  .post--training { left: 316px; }
  .post--blog     { left: 613px; }
  .post--facts    { left: 909px; }

  .post__photo { position: absolute; inset: 0; }
  .post--podcast  .post__photo { background: radial-gradient(circle at 72% 40%, #5b8fc2 0%, var(--podcast-mid) 30%, var(--podcast-deep) 75%); }
  .post--training .post__photo { background: radial-gradient(circle at 58% 42%, #9a9a9a 0%, var(--training-mid) 25%, var(--training-deep) 65%); }
  .post--blog     .post__photo { background: linear-gradient(150deg, #7d560f 0%, var(--blog-deep) 22%, var(--blog-mid) 60%, #f9c84a 100%); }
  .post--facts    .post__photo { background: linear-gradient(100deg, var(--facts-deep) 30%, var(--facts-mid) 72%, #cfe6d6 100%); }

  .post__shapes { position: absolute; inset: 0; width: 271px; height: 271px; }

  .post__brand { position: absolute; top: 25px; font-size: 12px; font-weight: 400; white-space: nowrap; }
  .post--podcast .post__brand, .post--training .post__brand { right: 20px; }
  .post--blog .post__brand, .post--facts .post__brand { left: 19px; }

  .post__intro { position: absolute; left: 21px; top: 24px; font-size: 14px; font-weight: 300; line-height: 15px; }

  .post__title { position: absolute; left: 19px; font-weight: 700; font-size: 22px; line-height: 21px; }
  .post--podcast  .post__title { top: 62px; text-transform: uppercase; }
  .post--training .post__title { top: 22px; text-transform: uppercase; }
  .post--blog     .post__title { top: 85px; }
  .post--facts    .post__title { top: 85px; }

  .post__meta { position: absolute; left: 21px; top: 94px; font-size: 14px; font-weight: 300; line-height: 15px; }

  .post__guest-photo {
    position: absolute; left: 16px; bottom: 16px; width: 44px; height: 44px; border-radius: 50%;
    background: radial-gradient(circle at 45% 40%, #6f9cc8 0%, #24507f 60%, #163a63 100%);
    border: 1.5px solid rgba(255,255,255,0.7);
  }
  .post__host { position: absolute; left: 68px; bottom: 22px; font-size: 9px; line-height: 10px; }

  .post__label { position: absolute; right: 18px; bottom: 66px; font-size: 10px; font-weight: 300; line-height: 10px; text-align: right; }
  .post__icon { position: absolute; right: 18px; bottom: 18px; width: 44px; height: 40px; }
</style>
</head>
<body>

<article class="post post--podcast">
  <div class="post__photo" role="img" aria-label="Portretfoto van de podcastgast in blauwe duotoon"></div>
  <svg class="post__shapes" viewBox="0 0 271 271" aria-hidden="true">
    <circle cx="271" cy="271" r="120" fill="var(--podcast-accent)"/>
    <path d="M0 200 C80 190 120 150 170 175" fill="none" stroke="var(--path-line)" stroke-width="1"/>
  </svg>
  <p class="post__brand">Bright Path Academy</p>
  <p class="post__intro">Kijk eens verder<br>met</p>
  <h2 class="post__title">Joris<br>Meerveld</h2>
  <div class="post__guest-photo" role="img" aria-label="Portretfoto van host Berend"></div>
  <p class="post__host">gehost door<br>Berend Valkhof</p>
  <p class="post__label">podcast</p>
  <svg class="post__icon" viewBox="0 0 44 40" fill="none" stroke="#fff" stroke-width="2" stroke-linecap="round" aria-hidden="true">
    <rect x="16" y="3" width="12" height="20" rx="6"/>
    <path d="M10 16 a12 12 0 0 0 24 0"/><line x1="22" y1="28" x2="22" y2="35"/><line x1="15" y1="36" x2="29" y2="36"/>
  </svg>
</article>

<article class="post post--training">
  <div class="post__photo" role="img" aria-label="Zwart-witportret van de trainer"></div>
  <svg class="post__shapes" viewBox="0 0 271 271" aria-hidden="true">
    <circle cx="271" cy="271" r="120" fill="var(--training-accent)"/>
    <path d="M0 220 C80 210 120 160 170 175" fill="none" stroke="var(--path-line)" stroke-width="1"/>
  </svg>
  <p class="post__brand">Bright Path Academy</p>
  <h2 class="post__title">Pre-new<br>year’s<br>eve</h2>
  <p class="post__meta">Dinsdag<br>29dec<br>19-21u</p>
  <p class="post__label">online<br>training</p>
  <svg class="post__icon" viewBox="0 0 44 40" fill="none" stroke="#fff" stroke-width="2" stroke-linecap="round" stroke-linejoin="round" aria-hidden="true">
    <rect x="4" y="4" width="36" height="24" rx="3"/>
    <line x1="15" y1="36" x2="29" y2="36"/><line x1="22" y1="28" x2="22" y2="36"/>
    <path d="M18 11 l9 5 -9 5 z" fill="#fff"/>
  </svg>
</article>

<article class="post post--blog">
  <div class="post__photo" role="img" aria-label="Foto van een notitieblok met handgeschreven voornemens en een pen"></div>
  <svg class="post__shapes" viewBox="0 0 271 271" aria-hidden="true">
    <circle cx="271" cy="271" r="120" fill="var(--blog-accent)"/>
    <path d="M0 230 C80 220 120 165 170 175" fill="none" stroke="var(--path-line)" stroke-width="1"/>
  </svg>
  <p class="post__brand">Bright Path Academy</p>
  <h2 class="post__title">Goede<br>Voornemens<br>die je volhoudt<br>3 tips</h2>
  <p class="post__label">blog</p>
  <svg class="post__icon" viewBox="0 0 44 40" fill="none" stroke="#fff" stroke-width="2" stroke-linecap="round" stroke-linejoin="round" aria-hidden="true">
    <path d="M8 34 l4 -10 L30 6 l6 6 L18 30 z"/><line x1="26" y1="10" x2="32" y2="16"/>
    <line x1="8" y1="37" x2="38" y2="37"/>
  </svg>
</article>

<article class="post post--facts">
  <div class="post__photo" role="img" aria-label="Foto van een peinzende vrouw in groene duotoon"></div>
  <svg class="post__shapes" viewBox="0 0 271 271" aria-hidden="true">
    <circle cx="271" cy="271" r="120" fill="var(--facts-accent)"/>
    <path d="M0 240 C80 230 120 170 170 175" fill="none" stroke="var(--path-line)" stroke-width="1"/>
  </svg>
  <p class="post__brand">Bright Path Academy</p>
  <h2 class="post__title">Gemiddeld<br>haalt slechts<br>20% zijn/haar<br>goede<br>voornemens</h2>
  <p class="post__label">facts</p>
  <svg class="post__icon" viewBox="0 0 44 40" fill="none" stroke="#fff" stroke-width="2" stroke-linecap="round" stroke-linejoin="round" aria-hidden="true">
    <path d="M22 4 a14 12 0 1 1 -6 23 l-8 5 2 -8 a14 12 0 0 1 12 -20 z"/>
    <line x1="22" y1="10" x2="22" y2="18"/><circle cx="22" cy="23" r="1.3" fill="#fff"/>
  </svg>
</article>

</body>
</html>
```